B2B Energy Broker Website

Our current website looks amateur, we need something far more professional looking and advanced. Current website is www.kelmora-utilitylink.com

```html
<!DOCTYPE html>
<html lang="en">
<head>
<meta charset="utf-8">
<title>Kelmora Utility Link – Transparent Energy Savings</title>
<link rel="stylesheet" href="https://fonts.googleapis.com/css2?family=Nunito:wght@300;400;600;700;800;900&display=swap">
<style>
:root{
  --navy:#1f2558;
  --navy-band:#252b5f;
  --blue:#2d68b0;
  --ink:#1d2147;
  --grey:#5c5f70;
  --line:#9fb3d6;
  --footer:#16181c;
  --map:#e6e7ea;
  --white:#ffffff;
}
*{box-sizing:border-box;margin:0;padding:0}
html,body{width:1200px;height:4169px;overflow:hidden}
body{position:relative;background:var(--white);font-family:"Nunito",sans-serif;color:var(--ink)}
.abs{position:absolute}
.page{left:129px;top:142px;width:943px;height:3881px;box-shadow:0 0 14px rgba(0,0,0,.12);background:var(--white)}

/* header */
.brand{display:flex;align-items:center;gap:10px}
.brand-dot{width:54px;height:54px;border-radius:50%;background:#4a4c52}
.brand-name{font-weight:400;color:#4a4c52;line-height:1.05}
.brand-name .big{font-size:25px;letter-spacing:7px;display:block}
.brand-name .small{font-size:15px;display:block}
.topline{font-size:12px;color:var(--ink);display:flex;gap:22px;align-items:center}
.topline span{display:flex;align-items:center;gap:6px}
.nav{display:flex;gap:32px;font-size:13px;font-weight:700;color:var(--ink)}
.nav .active{border-bottom:2px solid var(--ink);padding-bottom:4px}
.nav-rule{height:1px;background:#cfd3de}
.btn-contact{background:var(--navy);color:var(--white);font-size:12px;font-weight:800;display:flex;align-items:center;justify-content:center}

/* hero */
.hero{left:129px;top:230px;width:943px;height:376px;background:linear-gradient(120deg,#2a3566 0%,#3b5a8e 55%,#6d8fb9 100%)}
.hero-rule{left:207px;top:230px;width:1px;height:220px;background:rgba(255,255,255,.45)}
.hero-title{left:247px;top:330px;color:var(--white);font-size:33px;line-height:42px;font-weight:400;letter-spacing:.5px}
.hero-title b{font-weight:800}
.hero-sub{left:247px;top:427px;color:var(--white);font-size:20px;font-weight:300}
.hero-globe{left:641px;top:271px;width:292px;height:292px;border-radius:50%;border:9px solid #b9bdc6;background:radial-gradient(circle at 55% 60%,#5a4b2e 0%,#1b2233 45%,#0c1020 100%)}
.tab{background:var(--white)}

.cta-btn{display:flex;align-items:center}
.cta-btn .label{display:flex;align-items:center;justify-content:center;font-weight:800;font-size:12px;letter-spacing:.5px}
.cta-btn .knob{width:30px;height:30px;border-radius:50%;margin-left:-14px;display:flex;align-items:center;justify-content:center}
.solid .label{background:var(--blue);color:var(--white)}
.solid .knob{border:1.5px solid var(--white);background:var(--blue)}
.outline .label{border:1.5px solid var(--navy);color:var(--navy);background:var(--white)}
.outline .knob{background:var(--blue)}

/* welcome */
.kicker{font-size:18px;color:var(--ink)}
.title-lg{font-size:28px;font-weight:800;color:var(--navy)}
.underline{height:2px;background:var(--line)}
.welcome-disc{left:173px;top:820px;width:150px;height:150px;border-radius:50%;background:var(--blue)}
.welcome-photo{left:247px;top:778px;width:193px;height:236px;background:linear-gradient(170deg,#d6e3ef 0%,#a8bccf 50%,#6b7d8e 100%)}
.welcome-copy{left:513px;top:778px;width:398px;font-size:11.5px;line-height:17px;color:var(--grey);text-align:justify}
.welcome-copy p{margin-bottom:8px}
.welcome-copy b{color:var(--ink);font-weight:800}

/* services */
.band{left:129px;top:1088px;width:943px;height:754px;background:linear-gradient(90deg,var(--navy-band) 0%,#242a5d 60%,#2c3467 100%)}
.band-title{left:246px;top:1150px;color:var(--white);font-size:27px;line-height:36px;font-weight:800}
.band-rule{left:246px;top:1237px;width:104px;height:1px;background:#6e7aa8}
.service{width:250px;color:var(--white)}
.service-icon{width:64px;height:64px;border-radius:50%;background:var(--white);display:flex;align-items:center;justify-content:center}
.service-icon i{width:42px;height:42px;border-radius:50%;background:var(--blue);display:flex;align-items:center;justify-content:center}
.service h3{font-size:20px;font-weight:800;margin:14px 0 10px}
.service p{font-size:12.5px;line-height:19px;text-align:justify;color:#dfe2ee}

/* why */
.why-title{left:247px;top:1903px;font-size:28px;color:var(--navy);font-weight:400}
.why-title b{font-weight:900}
.why-item{width:264px;z-index:2}
.tick{width:56px;height:56px;border-radius:50%;background:var(--navy);border:4px solid #d7dbe6;display:flex;align-items:center;justify-content:center}
.why-item h4{font-size:16px;font-weight:800;color:var(--ink);margin-bottom:4px}
.why-item p{font-size:11.5px;line-height:17px;color:var(--grey);text-align:justify}
.worker{left:630px;top:1811px;width:442px;height:501px;background:linear-gradient(160deg,#ffffff 0%,#dfe3ea 30%,#7d6a5a 60%,#3b3e4a 100%);z-index:1}

.helped{left:0;top:2405px;width:1200px;text-align:center;font-size:21px;line-height:30px;color:var(--ink)}
.suppliers{left:262px;top:2522px;width:676px;display:flex;justify-content:space-between;align-items:center}
.supplier{font-weight:800;font-size:19px;color:#2f3a7a}

/* faq */
.faq{left:247px;top:2639px;width:705px;height:551px;background:var(--white);border:1px solid #e3e5ec}
.faq-title{left:247px;top:2688px;width:705px;text-align:center;font-size:22px;font-weight:900;color:var(--blue);letter-spacing:1px}
.faq-bar{left:293px;width:616px;height:73px;background:var(--navy);color:var(--white);font-size:12.5px;font-weight:800;letter-spacing:.4px;display:flex;align-items:center;justify-content:space-between;padding:0 24px;line-height:17px}
.caret{width:0;height:0;border-left:5px solid transparent;border-right:5px solid transparent;border-top:7px solid var(--white);flex:none}

/* map + cta */
.map{left:129px;top:3158px;width:943px;height:367px;background:linear-gradient(180deg,#e9eaec,#dcdde1)}
.cta-bar{left:251px;top:3287px;width:747px;height:107px;background:var(--navy);display:flex;align-items:center;padding-left:42px}
.cta-bar h2{color:var(--white);font-size:21px;font-weight:800}

/* footer */
.footer{left:129px;top:3525px;width:943px;height:498px;background:var(--footer)}
.f-disc{left:176px;top:3591px;width:120px;height:120px;border-radius:50%;background:#4a4c52}
.f-brand{left:150px;top:3732px;width:175px;text-align:center;color:#d9dadf;font-weight:400}
.f-brand .big{font-size:25px;letter-spacing:9px;display:block}
.f-brand .small{font-size:16px;display:block;margin-top:8px}
.f-head{font-size:23px;color:var(--white);font-weight:400}
.f-links{list-style:none;font-size:14px;color:#d9dadf}
.f-links li{height:37px}
.f-contact{font-size:14px;color:#d9dadf;line-height:19px}
.f-ico{width:28px;height:28px;border-radius:50%;border:1.5px solid #d9dadf;display:flex;align-items:center;justify-content:center}
.legal{left:129px;width:943px;text-align:center;color:#d9dadf;font-size:13.5px;line-height:18px}
</style>
</head>
<body>
<div class="abs page"></div>

<!-- header -->
<div class="abs brand" style="left:247px;top:157px">
  <div class="brand-dot"></div>
  <div class="brand-name"><span class="big">KELMORA</span><span class="small">utility link</span></div>
</div>
<div class="abs topline" style="left:676px;top:150px">
  <span><svg width="12" height="12" viewBox="0 0 24 24"><path d="M6.6 10.8a15 15 0 0 0 6.6 6.6l2.2-2.2a1 1 0 0 1 1-.25 11.4 11.4 0 0 0 3.6.6 1 1 0 0 1 1 1V20a1 1 0 0 1-1 1A17 17 0 0 1 3 4a1 1 0 0 1 1-1h3.5a1 1 0 0 1 1 1c0 1.25.2 2.45.6 3.6a1 1 0 0 1-.25 1z" fill="#1d2147"/></svg>0300 555 0142</span>
  <span><svg width="12" height="12" viewBox="0 0 24 24"><circle cx="12" cy="12" r="9" fill="none" stroke="#1d2147" stroke-width="2"/><circle cx="12" cy="12" r="4" fill="none" stroke="#1d2147" stroke-width="2"/></svg>info@kelmora-utilitylink.com</span>
</div>
<div class="abs nav-rule" style="left:594px;top:176px;width:433px"></div>
<nav class="abs nav" style="left:594px;top:195px">
  <span class="active">Home</span><span>About Us</span><span>Services</span><span>FAQs</span>
</nav>
<div class="abs btn-contact" style="left:920px;top:189px;width:107px;height:28px">Contact Us</div>

<!-- hero -->
<div class="abs hero" role="img" aria-label="Night-time view of Earth from orbit with city lights"></div>
<div class="abs hero-rule"></div>
<h1 class="abs hero-title">TRANSPARENT<br><b>ENERGY SAVINGS</b></h1>
<p class="abs hero-sub">Unbiased For your Business</p>
<div class="abs cta-btn solid" style="left:247px;top:487px">
  <div class="label" style="width:142px;height:42px">GET A QUOTE</div>
  <div class="knob"><svg width="14" height="10" viewBox="0 0 14 10"><path d="M0 5h12M8 1l4 4-4 4" fill="none" stroke="#fff" stroke-width="1.5"/></svg></div>
</div>
<div class="abs hero-globe" role="img" aria-label="Circular photo of a continent lit up at night"></div>
<div class="abs tab" style="left:129px;top:597px;width:312px;height:9px;border-radius:0 6px 0 0"></div>

<!-- welcome -->
<p class="abs kicker" style="left:247px;top:654px">Welcome To</p>
<h2 class="abs title-lg" style="left:247px;top:680px">KELMORA UTILITY LINK</h2>
<div class="abs underline" style="left:247px;top:736px;width:104px"></div>
<div class="abs welcome-disc"></div>
<div class="abs welcome-photo" role="img" aria-label="Two engineers in hard hats reviewing a tablet beside solar panels"></div>
<div class="abs welcome-copy">
  <p>Along with <b>providing competitive business energy procurement</b>, we run a <b>complete service solution for your ongoing energy requirements.</b></p>
  <p>We can take total management of your <b>bills, supplier relationship, renewals and more</b>.</p>
  <p>If you are concerned about a more complex arrangement for your energy supply, then we will endeavour to take over the time spent on it and allow you as much or as little involvement as you desire.</p>
</div>
<div class="abs cta-btn outline" style="left:513px;top:970px">
  <div class="label" style="width:126px;height:44px;font-size:10.5px">LEARN MORE</div>
  <div class="knob"><svg width="14" height="10" viewBox="0 0 14 10"><path d="M0 5h12M8 1l4 4-4 4" fill="none" stroke="#fff" stroke-width="1.5"/></svg></div>
</div>

<!-- services -->
<div class="abs band"></div>
<h2 class="abs band-title">Get More From<br>Our Energy Solutions</h2>
<div class="abs band-rule"></div>

<div class="abs service" style="left:435px;top:1312px">
  <div class="service-icon"><i><svg width="20" height="20" viewBox="0 0 20 20"><rect x="4" y="3" width="12" height="14" rx="1" fill="none" stroke="#fff" stroke-width="1.6"/><path d="M7 7h6M7 10h6M7 13h4" stroke="#fff" stroke-width="1.4"/></svg></i></div>
  <h3>Commercial Gas</h3>
  <p>We offer an impartial review of your business gas requirements to ensure you are getting the best prices, service and management as a total package.</p>
</div>
<div class="abs service" style="left:713px;top:1312px">
  <div class="service-icon"><i><svg width="20" height="20" viewBox="0 0 20 20"><circle cx="10" cy="9" r="5" fill="none" stroke="#fff" stroke-width="1.6"/><path d="M8 16h4M10 1v2M3 9H1M19 9h-2M4 3l1.4 1.4M16 3l-1.4 1.4" stroke="#fff" stroke-width="1.4"/></svg></i></div>
  <h3>Commercial Electricity</h3>
  <p>We offer an impartial review of your business electricity requirements to ensure you are getting the best prices, service and management as a total package.</p>
</div>
<div class="abs service" style="left:435px;top:1577px">
  <div class="service-icon"><i><svg width="20" height="20" viewBox="0 0 20 20"><path d="M4 16L14 6M6 4l10 10" stroke="#fff" stroke-width="2" stroke-linecap="round"/><circle cx="15" cy="5" r="2.5" fill="none" stroke="#fff" stroke-width="1.4"/></svg></i></div>
  <h3>Utility Services</h3>
  <p>We can provide a wide range of business utility management services to ensure your time and money is better spent.</p>
</div>
<div class="abs service" style="left:713px;top:1577px">
  <div class="service-icon"><i><svg width="20" height="20" viewBox="0 0 20 20"><path d="M10 2C7 7 5 10 5 13a5 5 0 0 0 10 0c0-3-2-6-5-11z" fill="#fff"/></svg></i></div>
  <h3>Commercial Water</h3>
  <p>The commercial water market has now been de-regulated. Speak to our team to find out how we can save you money on your water and waste bills.</p>
</div>
<div class="abs tab" style="left:247px;top:1830px;width:219px;height:12px;border-radius:6px 6px 0 0"></div>

<!-- why choose us -->
<div class="abs worker" role="img" aria-label="Engineer in a hard hat and safety harness holding a tablet"></div>
<h2 class="abs why-title">WHY <b>CHOOSE US</b></h2>
<div class="abs underline" style="left:247px;top:1949px;width:104px"></div>

<div class="abs tick" style="left:250px;top:1993px"><svg width="22" height="18" viewBox="0 0 22 18"><path d="M2 9l6 6L20 2" fill="none" stroke="#fff" stroke-width="3.5" stroke-linecap="round" stroke-linejoin="round"/></svg></div>
<div class="abs why-item" style="left:330px;top:1990px"><h4>Market Trend Analysis</h4><p>Our energy analysts monitor a live energy market curve to ensure you buy at the right time and save as much as possible.</p></div>

<div class="abs tick" style="left:250px;top:2116px"><svg width="22" height="18" viewBox="0 0 22 18"><path d="M2 9l6 6L20 2" fill="none" stroke="#fff" stroke-width="3.5" stroke-linecap="round" stroke-linejoin="round"/></svg></div>
<div class="abs why-item" style="left:330px;top:2111px"><h4>Direct Relationships</h4><p>We hold direct relationships with over 18 major suppliers, we use these relationships to ensure you get the most from you supplier.</p></div>

<div class="abs tick" style="left:250px;top:2237px"><svg width="22" height="18" viewBox="0 0 22 18"><path d="M2 9l6 6L20 2" fill="none" stroke="#fff" stroke-width="3.5" stroke-linecap="round" stroke-linejoin="round"/></svg></div>
<div class="abs why-item" style="left:330px;top:2234px"><h4>Industry Experience</h4><p>Our two founders hold over 30 years industry experience between them and our staff are what we believe to be the best in the industry.</p></div>

<p class="abs helped">We have helped businesses of all sizes<br>with our clean energy solutions, including:</p>
<div class="abs suppliers">
  <span class="supplier">Brightwell</span><span class="supplier">Norvale</span><span class="supplier">Ashby Gas</span><span class="supplier">Solvane</span><span class="supplier">Pellow</span><span class="supplier">Tidemark</span><span class="supplier">Ferrow</span>
</div>

<!-- map + faq -->
<div class="abs map" role="img" aria-label="Street map of the office area"></div>
<div class="abs faq"></div>
<h2 class="abs faq-title">FREQUENTLY ASKED QUESTIONS</h2>
<div class="abs faq-bar" style="top:2768px"><span>WHY SHOULD MY BUSINESS USE KELMORA UTILITY LINK?</span><i class="caret"></i></div>
<div class="abs faq-bar" style="top:2867px"><span>WHY SHOULD MY BUSINESS USE KELMORA UTILITY LINK?</span><i class="caret"></i></div>
<div class="abs faq-bar" style="top:2964px"><span>ONCE I HAVE SIGNED A CONTRACT, IS THERE A COOLING OFF PERIOD IF<br>I CHANGE MY MIND?</span><i class="caret"></i></div>
<div class="abs cta-btn outline" style="left:530px;top:3092px">
  <div class="label" style="width:126px;height:42px;font-size:10.5px">VIEW ALL</div>
  <div class="knob"><svg width="14" height="10" viewBox="0 0 14 10"><path d="M0 5h12M8 1l4 4-4 4" fill="none" stroke="#fff" stroke-width="1.5"/></svg></div>
</div>

<div class="abs cta-bar"><h2>Ready to have your energy needs taken care of?</h2></div>
<div class="abs cta-btn solid" style="left:865px;top:3322px">
  <div class="label" style="width:116px;height:36px;font-size:11px">GET A QUOTE</div>
  <div class="knob" style="width:26px;height:26px"><svg width="12" height="9" viewBox="0 0 14 10"><path d="M0 5h12M8 1l4 4-4 4" fill="none" stroke="#fff" stroke-width="1.5"/></svg></div>
</div>

<!-- footer -->
<div class="abs footer"></div>
<div class="abs f-disc"></div>
<div class="abs f-brand"><span class="big">KELMORA</span><span class="small">utility link</span></div>

<h3 class="abs f-head" style="left:393px;top:3584px">Menu</h3>
<ul class="abs f-links" style="left:393px;top:3654px"><li>Home</li><li>About Us</li><li>Services</li><li>FAQs</li></ul>
<h3 class="abs f-head" style="left:540px;top:3584px">Quick Links</h3>
<ul class="abs f-links" style="left:540px;top:3654px"><li>Privacy Policy</li><li>Cookie Policy</li><li>Terms &amp; Conditions</li></ul>
<h3 class="abs f-head" style="left:755px;top:3584px">Contacts</h3>

<div class="abs f-ico" style="left:756px;top:3656px"><svg width="12" height="14" viewBox="0 0 12 14"><path d="M6 13S1 8 1 5a5 5 0 0 1 10 0c0 3-5 8-5 8z" fill="none" stroke="#d9dadf" stroke-width="1.3"/><circle cx="6" cy="5" r="1.6" fill="#d9dadf"/></svg></div>
<p class="abs f-contact" style="left:805px;top:3654px">Unit 4,<br>12 Harrow Lane, Northfield,<br>NF2 7QA</p>
<div class="abs f-ico" style="left:756px;top:3730px"><svg width="13" height="13" viewBox="0 0 24 24"><path d="M6.6 10.8a15 15 0 0 0 6.6 6.6l2.2-2.2a1 1 0 0 1 1-.25 11.4 11.4 0 0 0 3.6.6 1 1 0 0 1 1 1V20a1 1 0 0 1-1 1A17 17 0 0 1 3 4a1 1 0 0 1 1-1h3.5a1 1 0 0 1 1 1c0 1.25.2 2.45.6 3.6a1 1 0 0 1-.25 1z" fill="#d9dadf"/></svg></div>
<p class="abs f-contact" style="left:805px;top:3735px">0300 555 0142</p>
<div class="abs f-ico" style="left:756px;top:3767px"><svg width="14" height="12" viewBox="0 0 14 12"><rect x="1" y="4" width="12" height="7" rx="1" fill="none" stroke="#d9dadf" stroke-width="1.3"/><rect x="3.5" y="1" width="7" height="3" fill="none" stroke="#d9dadf" stroke-width="1.3"/></svg></div>
<p class="abs f-contact" style="left:805px;top:3771px">0300 555 0142</p>
<div class="abs f-ico" style="left:756px;top:3805px"><svg width="13" height="13" viewBox="0 0 24 24"><circle cx="12" cy="12" r="9" fill="none" stroke="#d9dadf" stroke-width="2"/><circle cx="12" cy="12" r="4" fill="none" stroke="#d9dadf" stroke-width="2"/></svg></div>
<p class="abs f-contact" style="left:805px;top:3809px">info@kelmora-utilitylink.com</p>

<p class="abs legal" style="top:3906px">© Kelmora Utility Link 2022</p>
<p class="abs legal" style="top:3943px;padding:0 118px">All customer data will be retained securely in line with the data protection act. The data stored will only be used for the intended purposes of utility contracting and will be sent to the relevant supplier when necessary.</p>
</body>
</html>
```